Marlowe Ridge Holdings

I have a real estate investment business.

** I need editable vector files of the final design.

Industry/Entity Type

Real Estate

Contact Information for Business Card

I would like the card to be clear and direct with the company name and contact info. I would prefer not to have a design that is too busy (i.e., with excessive detail) in the business card.

Font styles to use
Sans Serif

Requirements
Must have
• My card must have the following information listed below:
• Company name: Marlowe Ridge Holdings LLC
• My name: Daniel Vestrap
• Phone number: (555) 218-9064
• Email address: dlvestrap@fernmail.example
• Keywords: “Real Estate Investments”
Nice to have
• I would like to have a design that resembles the characteristics/uses of obsidian stone which resembles something related to strength and resilience. Perhaps something with sharp, sleek color transitions as well.

```html
<!DOCTYPE html>
<html lang="en">
<head>
<meta charset="UTF-8">
<title>Marlowe Ridge Holdings LLC – Business Card</title>
<link rel="stylesheet" href="https://fonts.googleapis.com/css2?family=Montserrat:wght@400;500;600&display=swap">
<style>
  :root {
    --page-bg: #5e4a36;
    --stone-dark: #050505;
    --stone-mid: #1a1b1b;
    --stone-light: #3a3c3c;
    --gold: #e0c437;
    --gold-soft: #d8bd45;
    --white: #f2f2f2;
  }
  * { margin: 0; padding: 0; box-sizing: border-box; }
  html, body {
    width: 900px; height: 1200px; overflow: hidden;
    background: var(--page-bg);
    font-family: "Montserrat", Arial, sans-serif;
  }
  .canvas { position: relative; width: 900px; height: 1200px; }
  .card {
    position: absolute; left: 80px; width: 732px; height: 428px;
    border-radius: 22px; overflow: hidden;
    box-shadow: 0 6px 18px rgba(0,0,0,0.45);
  }
  .card--front { top: 130px; }
  .card--back { top: 645px; }
  .stone-texture {
    position: absolute; inset: 0;
    background:
      radial-gradient(ellipse at 48% 8%, var(--stone-light) 0%, transparent 22%),
      radial-gradient(ellipse at 20% 70%, var(--stone-mid) 0%, transparent 35%),
      radial-gradient(ellipse at 85% 40%, var(--stone-mid) 0%, transparent 40%),
      linear-gradient(135deg, var(--stone-dark), #111 50%, var(--stone-dark));
  }
  .company-lockup {
    position: absolute; text-align: center; color: var(--gold);
  }
  .company-name {
    font-weight: 600; letter-spacing: 0.5px; line-height: 1.1;
    text-transform: uppercase;
  }
  .lockup-rule { height: 2px; background: var(--gold-soft); margin: 8px auto; }
  .tagline {
    font-weight: 400; color: var(--gold-soft); text-transform: uppercase;
    letter-spacing: 0.3px;
  }
  .card--front .company-lockup { left: 72px; top: 170px; width: 284px; }
  .card--front .company-name { font-size: 26px; }
  .card--front .lockup-rule { width: 270px; }
  .card--front .tagline { font-size: 16.5px; }
  .card--back .company-lockup { left: 166px; top: 160px; width: 400px; }
  .card--back .company-name { font-size: 36px; }
  .card--back .lockup-rule { width: 336px; margin: 12px auto; }
  .card--back .tagline { font-size: 21px; }
  .divider {
    position: absolute; left: 379px; top: 182px; width: 1px; height: 93px;
    background: var(--gold-soft);
  }
  .contact { position: absolute; left: 407px; top: 160px; color: var(--white); }
  .contact-name {
    font-size: 20px; font-weight: 600; color: var(--gold);
    text-transform: uppercase; letter-spacing: 0.4px;
  }
  .contact-title {
    font-size: 15px; font-weight: 400; text-transform: uppercase;
    margin-top: 4px; letter-spacing: 0.3px;
  }
  .contact-line {
    display: flex; align-items: center; gap: 12px;
    font-size: 14.5px; margin-top: 6px;
  }
  .contact-line:first-of-type { margin-top: 16px; }
  .contact-icon { width: 15px; height: 13px; fill: var(--gold); flex: none; }
</style>
</head>
<body>
<main class="canvas">
  <section class="card card--front">
    <div class="stone-texture" role="img" aria-label="Polished black obsidian stone texture with grey veins"></div>
    <div class="company-lockup">
      <p class="company-name">Marlowe Ridge<br>Holdings LLC</p>
      <div class="lockup-rule"></div>
      <p class="tagline">Real Estate Investments</p>
    </div>
    <div class="divider"></div>
    <div class="contact">
      <p class="contact-name">Daniel Vestrap</p>
      <p class="contact-title">Managing Director</p>
      <p class="contact-line">
        <svg class="contact-icon" viewBox="0 0 24 24" aria-hidden="true"><path d="M6.6 10.8a15.1 15.1 0 0 0 6.6 6.6l2.2-2.2a1 1 0 0 1 1-.25 11.4 11.4 0 0 0 3.6.57 1 1 0 0 1 1 1V20a1 1 0 0 1-1 1A17 17 0 0 1 3 4a1 1 0 0 1 1-1h3.5a1 1 0 0 1 1 1c0 1.25.2 2.45.57 3.57a1 1 0 0 1-.25 1z"/></svg>
        (555) 218-9064
      </p>
      <p class="contact-line">
        <svg class="contact-icon" viewBox="0 0 24 20" aria-hidden="true"><path d="M1 2h22v16H1z M1 2l11 8 11-8" fill="var(--gold)" stroke="#000" stroke-width="1.5"/></svg>
        dlvestrap@fernmail.example
      </p>
    </div>
  </section>

  <section class="card card--back">
    <div class="stone-texture" role="img" aria-label="Polished black obsidian stone texture with grey veins"></div>
    <div class="company-lockup">
      <p class="company-name">Marlowe Ridge<br>Holdings LLC</p>
      <div class="lockup-rule"></div>
      <p class="tagline">Real Estate Investments</p>
    </div>
  </section>
</main>
</body>
</html>
```